CEDAR PEAK HEATING AND COOLING

Industry/Entity Type

Hvac

Requirements
Must have
• logo
My name: Tom Brennerov
Phone number 905-334-6071
Text:
Furnace and AC repairs
New furnace and AC installation
Ductwork
Gas lines
Water Tanks
Tankless water heaters
Nice to have
• Profesional modern look

```html
<!DOCTYPE html>
<html lang="en">
<head>
<meta charset="utf-8">
<title>Cedar Peak Heating and Cooling – Business Cards</title>
<link rel="stylesheet" href="https://fonts.googleapis.com/css2?family=Cinzel:wght@600&family=Montserrat:wght@400;500&display=swap">
<style>
  :root {
    --backdrop: #2a2a2a;
    --card-dark: #1f1f20;
    --card-dark-2: #3a3a3c;
    --card-light: #ffffff;
    --brand-blue: #1d5fae;
    --brand-green: #6cbd3c;
    --text-light: #f2f2f2;
    --text-dark: #2b2b2b;
  }
  * { box-sizing: border-box; margin: 0; padding: 0; }
  html, body { width: 1200px; height: 930px; overflow: hidden; }
  body {
    background: var(--backdrop);
    font-family: "Montserrat", sans-serif;
    position: relative;
  }
  .card {
    position: absolute;
    width: 560px;
    height: 320px;
    border-radius: 18px;
    overflow: hidden;
    box-shadow: 0 18px 40px rgba(0,0,0,.5);
  }

  /* Back card */
  .card--back {
    left: 90px; top: 90px;
    background: linear-gradient(135deg, var(--card-dark-2), var(--card-dark) 70%);
  }
  .card--back .wordmark {
    position: absolute; left: 60px; top: 88px;
    display: flex; align-items: center; gap: 14px;
  }
  .wordmark__dot {
    width: 22px; height: 22px; border-radius: 50%;
    background: var(--brand-green);
  }
  .wordmark__name {
    font-family: "Cinzel", serif; font-weight: 600;
    color: var(--brand-blue);
    font-size: 30px; line-height: 1.1; letter-spacing: 1px;
  }
  .wordmark__name small { display: block; font-size: 13px; letter-spacing: 2px; }
  .services {
    position: absolute; left: 60px; bottom: 52px;
    color: var(--text-light); font-size: 14.5px; line-height: 1.6;
  }
  .services .sep { color: var(--brand-green); padding: 0 5px; }

  /* Front card */
  .card--front {
    left: 560px; top: 520px;
    background: var(--card-light);
  }
  .card--front .bg { position: absolute; inset: 0; }
  .card--front .wordmark {
    position: absolute; left: 150px; top: 52px;
    display: flex; align-items: center; gap: 12px;
  }
  .card--front .wordmark__name { font-size: 28px; text-align: center; }
  .person {
    position: absolute; left: 140px; top: 238px; text-align: right; width: 200px;
  }
  .person__name {
    font-family: "Cinzel", serif; font-weight: 600;
    color: var(--brand-green); font-size: 19px; letter-spacing: 1px; white-space: nowrap;
  }
  .person__role { color: var(--text-light); font-size: 13px; margin-top: 2px; }
  .divider {
    position: absolute; left: 356px; top: 226px; width: 1.5px; height: 62px;
    background: var(--brand-green);
  }
  .contacts {
    position: absolute; left: 372px; top: 222px;
    list-style: none; color: var(--text-light); font-size: 12.5px; line-height: 1.65;
  }
  .contacts li { display: flex; align-items: center; gap: 7px; }
  .contacts svg { width: 11px; height: 11px; flex: none; }
</style>
</head>
<body>

<section class="card card--back" aria-label="Card back">
  <div class="wordmark">
    <span class="wordmark__dot"></span>
    <p class="wordmark__name">Cedar Peak<small>Heating and Cooling</small></p>
  </div>
  <p class="services">
    Furnace and AC repairs<span class="sep">|</span>New furnace and AC installation<br>
    Ductwork<span class="sep">|</span>Gas lines<span class="sep">|</span>Water Tanks<span class="sep">|</span>Tankless water heaters
  </p>
</section>

<section class="card card--front" aria-label="Card front">
  <svg class="bg" viewBox="0 0 560 320" preserveAspectRatio="none" aria-hidden="true">
    <path d="M0 320 L0 312 C110 200 300 150 560 118 L560 320 Z" fill="#1f1f20"/>
    <path d="M14 318 C110 196 300 140 560 100 L560 118 C300 152 120 205 24 318 Z" fill="#6cbd3c"/>
  </svg>
  <div class="wordmark">
    <span class="wordmark__dot"></span>
    <p class="wordmark__name">Cedar Peak<small>Heating and Cooling</small></p>
  </div>
  <div class="person">
    <p class="person__name">Tom Brennerov</p>
    <p class="person__role">Director</p>
  </div>
  <span class="divider"></span>
  <ul class="contacts">
    <li><svg viewBox="0 0 12 12"><path d="M3 1 L5 3.5 L4 5 C4.6 6.4 5.6 7.4 7 8 L8.5 7 L11 9 L10 11 C5.5 11 1 6.5 1 2 Z" fill="#1d5fae"/></svg>905-334-6071</li>
    <li><svg viewBox="0 0 12 12"><rect x="1" y="2.5" width="10" height="7" fill="none" stroke="#1d5fae" stroke-width="1.2"/><path d="M1 2.5 L6 6.5 L11 2.5" fill="none" stroke="#1d5fae" stroke-width="1.2"/></svg>info@cedarpeakhvac.com</li>
    <li><svg viewBox="0 0 12 12"><circle cx="6" cy="6" r="5" fill="none" stroke="#1d5fae" stroke-width="1.2"/><path d="M1 6 H11 M6 1 C3.5 4 3.5 8 6 11 C8.5 8 8.5 4 6 1" fill="none" stroke="#1d5fae" stroke-width="1"/></svg>www.cedarpeakhvac.com</li>
  </ul>
</section>

</body>
</html>
```